Verimont Designs business card

Front of card should be logo and back of card should be communication info.
Please note: reverse the logo color. Card should be black and everything else white.

Industry/Entity Type

Custom home design/construction

Contact Information for Business Card

Verimont Designs, LLC 614-382-9017 verimontdesigns@quillmail.example

Requirements
Must have
• Square card, Logo on front, communication info on back and perhaps a mini version of the logo on back also. Black card/white lettering. Double sides square card.
Nice to have
• I want to keep it simple. Our product (custom homes) speak for themselves.

```html
<!DOCTYPE html>
<html lang="en">
<head>
<meta charset="utf-8">
<title>Verimont Designs business card</title>
<link href="https://fonts.googleapis.com/css2?family=Montserrat:wght@400;500;600;700&display=swap" rel="stylesheet">
<style>
  :root {
    --page: #e4e4e4;
    --card-black: #232323;
    --band-grey: #808080;
    --paper-white: #ffffff;
    --ink-dark: #1e1e1e;
    --radius: 24px;
  }
  * { margin: 0; padding: 0; box-sizing: border-box; }
  html, body {
    width: 1200px; height: 900px; overflow: hidden;
    background: var(--page);
    font-family: "Montserrat", sans-serif;
  }
  .stage { position: relative; width: 1200px; height: 900px; }
  .card {
    position: absolute;
    width: 415px; height: 415px;
    border-radius: var(--radius);
    overflow: hidden;
    background: var(--card-black);
  }
  .card--contact { left: 120px; top: 246px; display: flex; flex-direction: column; }
  .card--brand { left: 605px; top: 245px; display: flex; align-items: center; justify-content: center; }

  .brand { text-align: center; color: var(--paper-white); }
  .brand__name {
    font-weight: 600; font-size: 28px; letter-spacing: 0.5px; line-height: 1;
    text-transform: uppercase;
  }
  .brand__tagline {
    display: flex; align-items: center; justify-content: center; gap: 12px;
    margin-top: 7px; font-size: 15px; font-weight: 500; letter-spacing: 0.6px;
  }
  .brand__tagline::before, .brand__tagline::after {
    content: ""; width: 38px; height: 1.5px; background: var(--paper-white);
  }

  .contact__brand { height: 225px; display: flex; align-items: center; justify-content: center; }
  .contact__people {
    height: 126px; background: var(--band-grey); color: var(--paper-white);
    display: flex; flex-direction: column; align-items: center; justify-content: center; gap: 4px;
  }
  .person { text-align: center; }
  .person + .person { margin-top: 6px; }
  .person__name { font-weight: 600; font-size: 19px; line-height: 1.3; }
  .person__phone {
    display: flex; align-items: center; justify-content: center; gap: 7px;
    font-size: 14px; margin-top: 3px;
  }
  .contact__mail {
    flex: 1; background: var(--paper-white); color: var(--ink-dark);
    display: flex; flex-direction: column; align-items: center; justify-content: center; gap: 6px;
  }
  .mail-rule { display: flex; align-items: center; gap: 6px; }
  .mail-rule::before, .mail-rule::after { content: ""; width: 80px; height: 1px; background: var(--ink-dark); }
  .mail-address { font-size: 14px; }
</style>
</head>
<body>
<main class="stage">
  <section class="card card--contact">
    <div class="contact__brand">
      <div class="brand">
        <div class="brand__name">Verimont Designs</div>
        <div class="brand__tagline">custom home builders</div>
      </div>
    </div>
    <div class="contact__people">
      <div class="person">
        <div class="person__name">Maren Holloway - CEO</div>
        <div class="person__phone">
          <svg width="16" height="16" viewBox="0 0 16 16" aria-hidden="true"><rect x="0.5" y="0.5" width="15" height="15" rx="3" fill="#fff"/><path d="M3.5 7.5c0-2 2-3 4.5-3s4.5 1 4.5 3l-2 .3-.4-1.4H5.9l-.4 1.4z M5 8.5h6l1 4H4z" fill="#808080"/></svg>
          <span>614-382-9017</span>
        </div>
      </div>
      <div class="person">
        <div class="person__name">Tobias Brandvik - GC</div>
        <div class="person__phone">
          <svg width="16" height="16" viewBox="0 0 16 16" aria-hidden="true"><rect x="0.5" y="0.5" width="15" height="15" rx="3" fill="#fff"/><path d="M3.5 7.5c0-2 2-3 4.5-3s4.5 1 4.5 3l-2 .3-.4-1.4H5.9l-.4 1.4z M5 8.5h6l1 4H4z" fill="#808080"/></svg>
          <span>302-618-4470</span>
        </div>
      </div>
    </div>
    <div class="contact__mail">
      <div class="mail-rule">
        <svg width="16" height="16" viewBox="0 0 16 16" aria-hidden="true"><rect x="0.5" y="0.5" width="15" height="15" rx="3" fill="#1e1e1e"/><rect x="3.5" y="4.5" width="9" height="7" rx="1" fill="#fff"/><path d="M3.8 5l4.2 3.3L12.2 5" fill="none" stroke="#1e1e1e" stroke-width="1.2"/></svg>
      </div>
      <div class="mail-address">verimontdesigns@quillmail.example</div>
    </div>
  </section>

  <section class="card card--brand">
    <div class="brand">
      <div class="brand__name">Verimont Designs</div>
      <div class="brand__tagline">custom home builders</div>
    </div>
  </section>
</main>
</body>
</html>
```